harvest Soon Book Cover Design for real estate investment book

I am looking for a Book Cover design for my new book. I would like designs for a hardcover, softcover and Lumora book.

The book deals with real estate and mortgage investments. Looking for a clean, bright simple design. Want to cover to be White with big RED letters. See "Dancing past Noon" book for an example ... see attached.

Target Market(s)

Affluent people with money looking for investment solutions.

Industry/Entity Type

Financial Service

Font styles to use
Serif

Requirements
Must have
• Bright clean design that will be appealing to affluent people.
• Title: harvest SOON
• Subtitle: A quiet method for thriving through land holdings
• subsubtitle: Secrets the Bank Teller Keeps Hidden From Clients...
• Author: Ned Falconby
• My Picture on the inside cover or on the back cover
• Book Description, Author description
Nice to have
• Focus on the Front cover look and feel first. Then we can look at the inside flaps and back cover. I will need to send you text. This is for the full cover. Front. Back. Spine. Inside flaps fro hardcover.

```html
<!DOCTYPE html>
<html lang="en">
<head>
<meta charset="utf-8">
<title>harvest SOON — Ned Falconby</title>
<link rel="stylesheet" href="https://fonts.googleapis.com/css2?family=Arvo:wght@700&family=Crimson+Text:ital@0;1&family=Cinzel:wght@400&display=swap">
<style>
  :root {
    --paper: #ffffff;
    --banner-red: #d81414;
    --title-red-light: #e8231f;
    --title-red-dark: #a30b0b;
    --ink: #1c1c1c;
    --rule-grey: #c8c8c8;
    --banner-text: #ffffff;
  }
  * { margin: 0; padding: 0; box-sizing: border-box; }
  html, body {
    width: 800px;
    height: 1200px;
    overflow: hidden;
    background: var(--paper);
  }
  .book-cover {
    position: relative;
    width: 800px;
    height: 1200px;
    background: var(--paper);
    overflow: hidden;
  }
  .teaser-band {
    position: absolute;
    top: 0; left: 0;
    width: 100%;
    height: 60px;
    background: linear-gradient(180deg, #e21a1a 0%, var(--banner-red) 60%, #b80d0d 100%);
    display: flex;
    align-items: center;
    padding-left: 32px;
  }
  .teaser-band__text {
    font-family: "Crimson Text", Georgia, serif;
    font-style: italic;
    font-size: 25px;
    color: var(--banner-text);
    letter-spacing: 0.2px;
  }
  .title {
    position: absolute;
    left: 0;
    width: 100%;
    text-align: center;
    font-family: "Arvo", "Rockwell", serif;
    font-weight: 700;
    background: linear-gradient(180deg, var(--title-red-light) 0%, #cf1515 55%, var(--title-red-dark) 100%);
    -webkit-background-clip: text;
    background-clip: text;
    color: transparent;
    white-space: nowrap;
  }
  .title--top {
    top: 130px;
    font-size: 172px;
    line-height: 1;
    letter-spacing: -4px;
  }
  .title--bottom {
    top: 365px;
    font-size: 245px;
    line-height: 1;
    letter-spacing: -2px;
  }
  .subtitle {
    position: absolute;
    top: 715px;
    left: 60px;
    width: 680px;
    text-align: center;
    font-family: "Crimson Text", Georgia, serif;
    font-size: 46px;
    line-height: 1.12;
    color: var(--ink);
  }
  .divider {
    position: absolute;
    top: 900px;
    left: 40px;
    width: 720px;
    height: 2px;
    background: var(--rule-grey);
  }
  .author {
    position: absolute;
    top: 955px;
    left: 0;
    width: 100%;
    text-align: center;
    font-family: "Cinzel", "Trajan Pro", serif;
    font-size: 66px;
    letter-spacing: 3px;
    color: var(--ink);
  }
</style>
</head>
<body>
  <main class="book-cover">
    <header class="teaser-band">
      <p class="teaser-band__text">Secrets the Bank Teller Keeps Hidden From Clients...</p>
    </header>

    <h1>
      <span class="title title--top">harvest</span>
      <span class="title title--bottom">SOON</span>
    </h1>

    <p class="subtitle">A quiet method for thriving through land holdings</p>

    <div class="divider"></div>

    <p class="author">Ned Falconby</p>
  </main>
</body>
</html>
```